To design a brand identity that is simple and creative with 'Valdor' as the brand name, I like modern simple fonts like helvetica neue, I want to print both sides of the card, I am open to dark front and white back, but the design needs to transfer well to letter heads and email signatures, I am looking for sophisticated and elegant, but open minded about clever and off the wall, I do not do 'boring' Valdor Holdings is the mother company for a small group, specialising in Management & consulting, Software development and construction, we have a high level of integrity, we are transparent and accountable for what we do. my images are provided as a guide only, Im not expecting them to be just copied, Im looking for a creator and passionate thinker, who will put life into their work.

Target Market(s)

usually business minded people who are looking for something different in me, such as leadership, confidence and focus with thinking that is per haps a little outside the box..

Industry/Entity Type

Construction

Requirements
Must have
• clean, minmalistic
Nice to have
• custom logo
Should not have
• boring, traditional

```html
<!DOCTYPE html>
<html lang="en">
<head>
<meta charset="utf-8">
<title>Valdor – Business Card</title>
<link rel="stylesheet" href="https://fonts.googleapis.com/css2?family=Inter:wght@300;400&display=swap">
<style>
  :root {
    --backdrop: #3b3634;
    --paper: #ffffff;
    --paper-shade: #e9e9e9;
    --ink: #111111;
    --ink-soft: #222222;
    --accent: #d9452b;
    --dot: #d42020;
    --mark: #e9a23b;
    --watermark: rgba(120, 120, 120, 0.4);
    --night: #2b2b2b;
    --night-deep: #1c1c1c;
    --night-text: #f2f2f2;
    --font: "Inter", "Helvetica Neue", Arial, sans-serif;
  }
  * { box-sizing: border-box; margin: 0; padding: 0; }
  html, body {
    width: 1000px; height: 1200px; overflow: hidden;
    background: var(--backdrop);
    font-family: var(--font);
  }
  .canvas { position: relative; width: 1000px; height: 1200px; }

  .card {
    position: absolute;
    width: 740px; height: 456px;
    overflow: hidden;
    box-shadow: 0 6px 18px rgba(0, 0, 0, 0.45);
  }
  .card-texture { position: absolute; inset: 0; }

  /* Front */
  .card-front { left: 136px; top: 75px; background: var(--paper); }
  .card-front .card-texture {
    background: radial-gradient(ellipse at 50% 45%, var(--paper) 0%, #f6f6f6 55%, var(--paper-shade) 100%);
  }
  .holder { position: absolute; right: 43px; top: 52px; text-align: right; color: var(--ink); }
  .holder-name { font-size: 25px; font-weight: 400; line-height: 1.1; }
  .holder-role { font-size: 15px; font-weight: 400; margin-top: 2px; }

  .brand {
    position: absolute; left: 0; right: 0;
    display: flex; align-items: center; justify-content: center; gap: 16px;
  }
  .brand-dot { border-radius: 50%; background: var(--mark); flex: none; }
  .brand-name { font-weight: 300; line-height: 1; }

  .card-front .brand { top: 150px; }
  .card-front .brand-dot { width: 44px; height: 44px; }
  .card-front .brand-name { font-size: 54px; color: var(--ink); }
  .tagline {
    position: absolute; left: 338px; top: 209px;
    font-size: 13px; color: var(--ink-soft);
  }

  .contact { position: absolute; left: 0; right: 0; text-align: center; font-size: 19px; color: var(--ink-soft); }
  .contact-line-1 { top: 252px; }
  .contact-line-2 { top: 286px; }
  .contact-item + .contact-item { margin-left: 18px; }
  .label { color: var(--accent); }

  .watermark {
    position: absolute; left: 0; right: 0; top: 318px;
    text-align: center; font-size: 84px; font-weight: 300;
    color: var(--watermark); line-height: 1;
  }
  .services {
    position: absolute; left: 0; right: 0; z-index: 1;
    text-align: center; font-size: 16px; letter-spacing: 1.2px; line-height: 1.2;
  }
  .services .sep { color: var(--dot); margin: 0 7px; font-size: 7px; vertical-align: middle; }
  .card-front .services { top: 356px; color: var(--ink); }

  /* Back */
  .card-back { left: 117px; top: 652px; background: var(--night); }
  .card-back .card-texture {
    background: radial-gradient(ellipse at 45% 55%, #3a3a3a 0%, var(--night) 45%, var(--night-deep) 100%);
  }
  .card-back .brand { top: 172px; height: 100px; gap: 22px; }
  .card-back .brand-dot { width: 92px; height: 92px; }
  .card-back .brand-name { font-size: 100px; color: var(--night-text); }
  .card-back .services { top: 297px; color: var(--night-text); }
  .web { position: absolute; left: 0; right: 0; top: 326px; text-align: center; font-size: 18px; letter-spacing: 0.6px; color: #d8d8d8; }
</style>
</head>
<body>
<main class="canvas">

  <section class="card card-front" aria-label="Card front">
    <div class="card-texture" role="img" aria-label="Soft white faceted polygon background pattern"></div>

    <div class="holder">
      <p class="holder-name">Mara Lind</p>
      <p class="holder-role">client ambassador</p>
    </div>

    <div class="brand">
      <span class="brand-dot"></span>
      <span class="brand-name">valdor</span>
    </div>
    <p class="tagline">... in the creation business</p>

    <p class="contact contact-line-1">
      <span class="contact-item"><span class="label">c.</span> +61 0400 517 264</span>
      <span class="contact-item"><span class="label">e.</span> info@valdor.com.au</span>
    </p>
    <p class="contact contact-line-2">
      <span class="contact-item"><span class="label">a.</span> po box 412 westbrook 6100</span>
    </p>

    <p class="watermark" aria-hidden="true">valdor</p>
    <p class="services">management<span class="sep">●</span>software<span class="sep">●</span>construction</p>
  </section>

  <section class="card card-back" aria-label="Card back">
    <div class="card-texture" role="img" aria-label="Dark charcoal faceted polygon background pattern"></div>

    <div class="brand">
      <span class="brand-dot"></span>
      <span class="brand-name">valdor</span>
    </div>

    <p class="services">management<span class="sep">●</span>software<span class="sep">●</span>construction</p>
    <p class="web"><span class="label">w.</span> www.valdor.holdings</p>
  </section>

</main>
</body>
</html>
```